Networking Events Calendar/Diary

We need a responsive website that can act as both an online diary/calendar and a resource for community and networking events similar to lookupmixerdates.com (we do not want a clone, but one with similar functionality). We need to be able to host adverts, have a client area for clients to add their own events to the diary. This needs to have the functionality that clients have to pay to add recurring events. Some integration would be useful so that if a clients already has their own online diary on their website then using an API possibly to also add that event into our online diary

Industry/Entity Type

Events

Coding

Coded - Design and coding required

Number of Pages Required

5+ page

Requirements
Must have
• My project must have a calendar area, space for ads, be responsive and easily viewable on mobile. A subscribers area for clients and a way to purchase premium status so that premium events are highlighted.

```html
<!DOCTYPE html>
<html lang="en">
<head>
<meta charset="utf-8">
<title>Gather Diary — Networking Events Calendar</title>
<link rel="stylesheet" href="https://fonts.googleapis.com/css2?family=Open+Sans:wght@400;600;700&family=PT+Sans:wght@400;700&display=swap">
<style>
:root{
  --grad-start:#8c4a80;
  --grad-mid:#ea5868;
  --grad-end:#ff7a35;
  --coral:#f4604a;
  --orange:#f2890f;
  --grey-badge:#b5b5b5;
  --page:#f4f4f4;
  --nav:#e6e6e6;
  --card:#ffffff;
  --ink:#222222;
  --text:#444444;
  --muted:#8a8a8a;
  --line:#dcdcdc;
  --white:#ffffff;
}
*{box-sizing:border-box;margin:0;padding:0}
html,body{width:1200px;height:2553px;overflow:hidden}
body{font-family:"Open Sans",Arial,sans-serif;background:var(--page);color:var(--text);position:relative}
a{color:inherit;text-decoration:none}

/* Hero */
.hero{position:absolute;left:0;top:0;width:1200px;height:541px;
  background:linear-gradient(90deg,var(--grad-start) 0%,var(--grad-mid) 45%,var(--grad-end) 100%);color:var(--white)}
.topbar{position:absolute;left:0;top:0;width:100%;height:51px;border-bottom:1px solid rgba(255,255,255,.25)}
.social{position:absolute;left:172px;top:16px;display:flex;gap:8px}
.social span{width:18px;height:18px;border:1px solid rgba(255,255,255,.7);border-radius:50%}
.toplinks{position:absolute;left:280px;top:17px;display:flex;gap:20px;font-size:12.5px;opacity:.9}
.search{position:absolute;left:879px;top:12px;width:148px;height:27px;border:1px solid rgba(255,255,255,.6);border-radius:14px;font-size:10px;padding:6px 12px;opacity:.85}
.search svg{position:absolute;right:10px;top:7px}
.brand{position:absolute;left:172px;top:110px;display:flex;align-items:center;gap:14px}
.brand .mark{width:46px;height:46px;border:4px solid var(--white);border-radius:4px}
.brand .name{font-family:"PT Sans",sans-serif;font-size:34px;font-weight:400;letter-spacing:.5px;line-height:1}
.welcome{position:absolute;left:172px;top:224px;width:380px;font-size:13.5px;line-height:22px}
.welcome h2{font-size:13.5px;font-weight:700}
.hero-action{position:absolute;left:172px;display:flex;align-items:center;gap:18px;font-size:14px;font-weight:700}
.hero-action.register{top:400px}
.hero-action.subscribe{top:449px}

.calendar{position:absolute;left:648px;top:105px;width:380px}
.cal-head{display:flex;justify-content:space-between;align-items:center;font-family:"PT Sans",sans-serif}
.cal-head h3{font-size:15.5px;font-weight:700;padding-left:21px}
.cal-head .create{font-size:10px;font-weight:700;display:flex;align-items:center;gap:8px}
.cal-controls{display:flex;align-items:center;margin-top:26px;padding-left:21px;font-family:"PT Sans",sans-serif;position:relative;height:26px}
.cal-controls .arrows{display:flex;gap:14px}
.today{margin-left:18px;border:1px solid var(--white);border-radius:3px;font-size:9.5px;font-weight:700;padding:3px 6px}
.month{margin-left:18px;font-size:15px;font-weight:700}
.views{position:absolute;right:4px;top:0;display:flex;border:1px solid var(--white);border-radius:3px;font-size:10px;overflow:hidden}
.views span{padding:4px 6px;border-left:1px solid var(--white)}
.views span:first-child{border-left:0;background:var(--white);color:var(--grad-mid)}
.cal-grid{display:grid;grid-template-columns:repeat(7,56.3px);margin-top:16px;text-align:center;font-size:14px}
.cal-grid .dow{font-weight:700;font-size:13px;height:54px;line-height:30px}
.cal-grid .day{height:54px;display:flex;justify-content:center}
.cal-grid .day span{width:30px;height:30px;line-height:30px;border-radius:50%}
.cal-grid .other{opacity:.55}
.cal-grid .today-day span{background:var(--white);color:var(--grad-mid);font-weight:700}
.cal-grid .marked span{border:1px solid var(--white);line-height:28px}

/* Nav */
.mainnav{position:absolute;left:0;top:541px;width:1200px;height:51px;background:var(--nav);font-size:13px;color:#555}
.mainnav a{position:absolute;top:16px;transform:translateX(-50%);white-space:nowrap}

/* Sections */
.section-title{position:absolute;display:flex;align-items:center;gap:12px;font-size:17px;font-weight:700;color:var(--ink);text-transform:uppercase}
.card{position:absolute;background:var(--card);border-radius:5px;box-shadow:0 1px 3px rgba(0,0,0,.08)}
.event-list{left:172px;width:512px;padding-top:23px}
.event{display:flex;height:102px;padding-left:24px}
.badge{width:70px;height:70px;border-radius:3px;overflow:hidden;text-align:center;color:var(--white);flex:none}
.badge .m{height:24px;line-height:25px;font-size:14px;background:var(--orange);border-bottom:1px solid rgba(255,255,255,.85)}
.badge .d{height:46px;line-height:44px;font-size:27px;font-weight:700;background:var(--orange)}
.event.regular .badge .m,.event.regular .badge .d{background:var(--grey-badge)}
.event-info{margin-left:18px;padding-top:0}
.event-info h4{font-size:14px;font-weight:600;color:#333;line-height:20px;margin-top:-4px}
.event-info p{font-size:10.5px;color:#555;display:flex;align-items:center;gap:8px;margin-top:8px}
.event-info p + p{margin-top:7px}

/* Forms */
.form{left:710px;width:318px;padding:13px 12px}
.field{height:41px;border:1px solid var(--line);border-radius:4px;font-size:12px;color:var(--muted);padding:12px 13px}
.btn{background:var(--coral);color:var(--white);border-radius:4px;font-size:13px;font-weight:700;text-align:center}
.login-row{display:flex;gap:14px;margin-top:13px}
.login-row .field{width:180px}
.login-row .btn{width:100px;height:41px;line-height:41px}
.remember{font-size:11px;color:var(--muted);margin-top:11px;display:flex;align-items:center;gap:8px}
.remember .box{width:10px;height:10px;border:1px solid #bbb}
.remember .forgot{color:var(--coral)}
.signup h3{text-align:center;font-size:18px;color:var(--ink);margin:11px 0 18px;font-weight:700}
.signup h3 span{font-size:14px;color:#aaa;font-weight:400}
.signup .field{margin-bottom:13px}
.signup .btn{width:172px;height:41px;line-height:41px;margin-left:auto}

.ads-slot{position:absolute;left:710px;top:1198px;width:318px;height:198px;background:#e8e8e8}
.premium{position:absolute;left:710px;top:1470px;width:318px}
.premium .lead{color:var(--orange);font-size:13.5px;font-weight:600;line-height:20px}
.premium .body{font-size:13.5px;color:#333;line-height:19px;margin-top:14px}
.btn-outline{display:inline-block;margin-top:29px;width:146px;height:38px;line-height:36px;border:1px solid var(--orange);border-radius:4px;color:var(--orange);font-size:13px;text-align:center}

/* Blog */
.blog{position:absolute;left:0;top:1940px;width:1200px;height:457px;background:var(--white)}
.post{position:absolute;top:31px;width:270px}
.post .photo{height:192px;background:radial-gradient(ellipse at 45% 70%,#8a6a3e 0%,#4a3422 45%,#1e1610 100%)}
.post .cat{font-size:9.5px;font-weight:700;color:var(--coral);margin-top:20px;text-transform:uppercase}
.post h4{font-size:18px;font-weight:700;color:var(--ink);line-height:21px;margin-top:9px;width:210px;text-transform:uppercase}
.post .date{font-size:13px;color:#333;margin-top:12px}
.post .excerpt{font-size:12.5px;color:#333;line-height:19px;margin-top:13px;width:240px}
.read-blog{position:absolute;left:526px;top:2430px;width:148px;height:36px;line-height:36px;font-size:12px;font-weight:600}

.footer{position:absolute;left:0;top:2498px;width:1200px;height:55px;border-top:1px solid var(--line);font-size:11.5px;color:var(--muted)}
.footer .copy{position:absolute;left:172px;top:24px}
.footer nav{position:absolute;right:173px;top:24px;display:flex;gap:32px;color:var(--coral)}
</style>
</head>
<body>

<header class="hero">
  <div class="topbar">
    <div class="social"><span></span><span></span><span></span></div>
    <nav class="toplinks"><a>Login</a><a>Contact Us</a><a>Tell a Friend</a><a>Useful Links</a></nav>
    <div class="search">search
      <svg width="11" height="11" viewBox="0 0 11 11" fill="none" stroke="#fff" stroke-width="1.3"><circle cx="4.5" cy="4.5" r="3.5"/><path d="M7 7l3 3"/></svg>
    </div>
  </div>

  <div class="brand"><span class="mark"></span><span class="name">GATHER DIARY</span></div>

  <div class="welcome">
    <h2>Welcome to Gather Diary</h2>
    <p>Welcome to the online resource offering a simple, quick way to access information about Business Networking Events, Business Clubs, Workshops, Seminars and Business Shows happening in your local area.</p>
  </div>

  <a class="hero-action register">
    <svg width="24" height="24" viewBox="0 0 24 24" fill="none" stroke="#fff" stroke-width="2"><circle cx="12" cy="12" r="10"/><path d="M12 7v10M7 12h10"/></svg>
    Register to Add Events
  </a>
  <a class="hero-action subscribe">
    <svg width="24" height="24" viewBox="0 0 24 24" fill="#fff"><circle cx="4" cy="20" r="3"/><path d="M1 10a13 13 0 0 1 13 13h-4A9 9 0 0 0 1 14z"/><path d="M1 2a21 21 0 0 1 21 21h-4A17 17 0 0 0 1 6z"/></svg>
    Subscribe to our Event Bulletin
  </a>

  <section class="calendar">
    <div class="cal-head">
      <h3>EVENTS CALENDAR</h3>
      <span class="create">CREATE YOUR EVENT
        <svg width="16" height="16" viewBox="0 0 16 16" fill="none" stroke="#fff" stroke-width="1.4"><circle cx="8" cy="8" r="7"/><path d="M8 4.5v7M4.5 8h7"/></svg>
      </span>
    </div>
    <div class="cal-controls">
      <span class="arrows">
        <svg width="10" height="14" viewBox="0 0 10 14" fill="none" stroke="#fff" stroke-width="2"><path d="M8 1L2 7l6 6"/></svg>
        <svg width="10" height="14" viewBox="0 0 10 14" fill="none" stroke="#fff" stroke-width="2"><path d="M2 1l6 6-6 6"/></svg>
      </span>
      <span class="today">TODAY</span>
      <span class="month">September 2015</span>
      <span class="views"><span>Month</span><span>Week</span><span>Day</span></span>
    </div>
    <div class="cal-grid">
      <div class="dow">S</div><div class="dow">M</div><div class="dow">T</div><div class="dow">W</div><div class="dow">T</div><div class="dow">F</div><div class="dow">S</div>
      <div class="day other"><span>29</span></div><div class="day other"><span>30</span></div><div class="day today-day"><span>1</span></div><div class="day"><span>2</span></div><div class="day"><span>3</span></div><div class="day"><span>4</span></div><div class="day"><span>5</span></div>
      <div class="day"><span>6</span></div><div class="day"><span>7</span></div><div class="day"><span>8</span></div><div class="day marked"><span>9</span></div><div class="day"><span>10</span></div><div class="day"><span>11</span></div><div class="day"><span>12</span></div>
      <div class="day"><span>13</span></div><div class="day"><span>14</span></div><div class="day marked"><span>15</span></div><div class="day"><span>16</span></div><div class="day"><span>17</span></div><div class="day"><span>18</span></div><div class="day"><span>19</span></div>
      <div class="day"><span>20</span></div><div class="day"><span>21</span></div><div class="day"><span>22</span></div><div class="day"><span>23</span></div><div class="day"><span>24</span></div><div class="day"><span>25</span></div><div class="day"><span>26</span></div>
      <div class="day"><span>27</span></div><div class="day"><span>28</span></div><div class="day"><span>29</span></div><div class="day"><span>30</span></div><div class="day"><span>31</span></div><div class="day other"><span>1</span></div><div class="day other"><span>2</span></div>
    </div>
  </section>
</header>

<nav class="mainnav">
  <a style="left:279px">Homepage</a>
  <a style="left:373px">What we do</a>
  <a style="left:536px">Events by location/Region</a>
  <a style="left:706px">Business Shows</a>
  <a style="left:831px">Concerts</a>
  <a style="left:941px">Contact Us</a>
</nav>

<h2 class="section-title" style="left:172px;top:628px">
  <svg width="18" height="18" viewBox="0 0 18 18" fill="none" stroke="#f2890f" stroke-width="2"><rect x="2" y="3" width="14" height="13" rx="1"/><path d="M2 7h14M6 1v4M12 1v4"/><rect x="7" y="9.5" width="4" height="3.5" fill="#f2890f" stroke="none"/></svg>
  Premium Events
</h2>

<div class="card event-list" style="top:683px;height:527px">
  <article class="event"><div class="badge"><div class="m">DEC</div><div class="d">13</div></div><div class="event-info"><h4>Brew &amp; Connect - Elmford Market</h4><p><svg width="11" height="11" viewBox="0 0 11 11" fill="none" stroke="#444" stroke-width="1.2"><circle cx="5.5" cy="5.5" r="4.6"/><path d="M5.5 3v2.7l1.8 1.2"/></svg>Tuesday ,10:00am - 11:30am</p><p><svg width="11" height="12" viewBox="0 0 11 12" fill="#444"><path d="M5.5 0A4 4 0 0 0 1.5 4c0 3 4 8 4 8s4-5 4-8a4 4 0 0 0-4-4zm0 5.6A1.6 1.6 0 1 1 5.5 2.4a1.6 1.6 0 0 1 0 3.2z"/></svg>Elmford Market, Mill Place , Elmford , Elmford , EF17 2RN</p></div></article>
  <article class="event"><div class="badge"><div class="m">DEC</div><div class="d">13</div></div><div class="event-info"><h4>Brew &amp; Connect - Elmford Market</h4><p><svg width="11" height="11" viewBox="0 0 11 11" fill="none" stroke="#444" stroke-width="1.2"><circle cx="5.5" cy="5.5" r="4.6"/><path d="M5.5 3v2.7l1.8 1.2"/></svg>Tuesday ,10:00am - 11:30am</p><p><svg width="11" height="12" viewBox="0 0 11 12" fill="#444"><path d="M5.5 0A4 4 0 0 0 1.5 4c0 3 4 8 4 8s4-5 4-8a4 4 0 0 0-4-4zm0 5.6A1.6 1.6 0 1 1 5.5 2.4a1.6 1.6 0 0 1 0 3.2z"/></svg>Elmford Market, Mill Place , Elmford , Elmford , EF17 2RN</p></div></article>
  <article class="event"><div class="badge"><div class="m">DEC</div><div class="d">13</div></div><div class="event-info"><h4>Brew &amp; Connect - Elmford Market</h4><p><svg width="11" height="11" viewBox="0 0 11 11" fill="none" stroke="#444" stroke-width="1.2"><circle cx="5.5" cy="5.5" r="4.6"/><path d="M5.5 3v2.7l1.8 1.2"/></svg>Tuesday ,10:00am - 11:30am</p><p><svg width="11" height="12" viewBox="0 0 11 12" fill="#444"><path d="M5.5 0A4 4 0 0 0 1.5 4c0 3 4 8 4 8s4-5 4-8a4 4 0 0 0-4-4zm0 5.6A1.6 1.6 0 1 1 5.5 2.4a1.6 1.6 0 0 1 0 3.2z"/></svg>Elmford Market, Mill Place , Elmford , Elmford , EF17 2RN</p></div></article>
  <article class="event"><div class="badge"><div class="m">DEC</div><div class="d">13</div></div><div class="event-info"><h4>Brew &amp; Connect - Elmford Market</h4><p><svg width="11" height="11" viewBox="0 0 11 11" fill="none" stroke="#444" stroke-width="1.2"><circle cx="5.5" cy="5.5" r="4.6"/><path d="M5.5 3v2.7l1.8 1.2"/></svg>Tuesday ,10:00am - 11:30am</p><p><svg width="11" height="12" viewBox="0 0 11 12" fill="#444"><path d="M5.5 0A4 4 0 0 0 1.5 4c0 3 4 8 4 8s4-5 4-8a4 4 0 0 0-4-4zm0 5.6A1.6 1.6 0 1 1 5.5 2.4a1.6 1.6 0 0 1 0 3.2z"/></svg>Elmford Market, Mill Place , Elmford , Elmford , EF17 2RN</p></div></article>
  <article class="event"><div class="badge"><div class="m">DEC</div><div class="d">13</div></div><div class="event-info"><h4>Brew &amp; Connect - Elmford Market</h4><p><svg width="11" height="11" viewBox="0 0 11 11" fill="none" stroke="#444" stroke-width="1.2"><circle cx="5.5" cy="5.5" r="4.6"/><path d="M5.5 3v2.7l1.8 1.2"/></svg>Tuesday ,10:00am - 11:30am</p><p><svg width="11" height="12" viewBox="0 0 11 12" fill="#444"><path d="M5.5 0A4 4 0 0 0 1.5 4c0 3 4 8 4 8s4-5 4-8a4 4 0 0 0-4-4zm0 5.6A1.6 1.6 0 1 1 5.5 2.4a1.6 1.6 0 0 1 0 3.2z"/></svg>Elmford Market, Mill Place , Elmford , Elmford , EF17 2RN</p></div></article>
</div>

<h2 class="section-title" style="left:172px;top:1245px">
  <svg width="18" height="18" viewBox="0 0 18 18" fill="none" stroke="#999" stroke-width="2"><rect x="2" y="3" width="14" height="13" rx="1"/><path d="M2 7h14M6 1v4M12 1v4"/><rect x="7" y="9.5" width="4" height="3.5" fill="#999" stroke="none"/></svg>
  Events
</h2>

<div class="card event-list" style="top:1302px;height:528px">
  <article class="event regular"><div class="badge"><div class="m">DEC</div><div class="d">13</div></div><div class="event-info"><h4>Brew &amp; Connect - Elmford Market</h4><p><svg width="11" height="11" viewBox="0 0 11 11" fill="none" stroke="#444" stroke-width="1.2"><circle cx="5.5" cy="5.5" r="4.6"/><path d="M5.5 3v2.7l1.8 1.2"/></svg>Tuesday ,10:00am - 11:30am</p><p><svg width="11" height="12" viewBox="0 0 11 12" fill="#444"><path d="M5.5 0A4 4 0 0 0 1.5 4c0 3 4 8 4 8s4-5 4-8a4 4 0 0 0-4-4zm0 5.6A1.6 1.6 0 1 1 5.5 2.4a1.6 1.6 0 0 1 0 3.2z"/></svg>Elmford Market, Mill Place , Elmford , Elmford , EF17 2RN</p></div></article>
  <article class="event regular"><div class="badge"><div class="m">DEC</div><div class="d">13</div></div><div class="event-info"><h4>Brew &amp; Connect - Elmford Market</h4><p><svg width="11" height="11" viewBox="0 0 11 11" fill="none" stroke="#444" stroke-width="1.2"><circle cx="5.5" cy="5.5" r="4.6"/><path d="M5.5 3v2.7l1.8 1.2"/></svg>Tuesday ,10:00am - 11:30am</p><p><svg width="11" height="12" viewBox="0 0 11 12" fill="#444"><path d="M5.5 0A4 4 0 0 0 1.5 4c0 3 4 8 4 8s4-5 4-8a4 4 0 0 0-4-4zm0 5.6A1.6 1.6 0 1 1 5.5 2.4a1.6 1.6 0 0 1 0 3.2z"/></svg>Elmford Market, Mill Place , Elmford , Elmford , EF17 2RN</p></div></article>
  <article class="event regular"><div class="badge"><div class="m">DEC</div><div class="d">13</div></div><div class="event-info"><h4>Brew &amp; Connect - Elmford Market</h4><p><svg width="11" height="11" viewBox="0 0 11 11" fill="none" stroke="#444" stroke-width="1.2"><circle cx="5.5" cy="5.5" r="4.6"/><path d="M5.5 3v2.7l1.8 1.2"/></svg>Tuesday ,10:00am - 11:30am</p><p><svg width="11" height="12" viewBox="0 0 11 12" fill="#444"><path d="M5.5 0A4 4 0 0 0 1.5 4c0 3 4 8 4 8s4-5 4-8a4 4 0 0 0-4-4zm0 5.6A1.6 1.6 0 1 1 5.5 2.4a1.6 1.6 0 0 1 0 3.2z"/></svg>Elmford Market, Mill Place , Elmford , Elmford , EF17 2RN</p></div></article>
  <article class="event regular"><div class="badge"><div class="m">DEC</div><div class="d">13</div></div><div class="event-info"><h4>Brew &amp; Connect - Elmford Market</h4><p><svg width="11" height="11" viewBox="0 0 11 11" fill="none" stroke="#444" stroke-width="1.2"><circle cx="5.5" cy="5.5" r="4.6"/><path d="M5.5 3v2.7l1.8 1.2"/></svg>Tuesday ,10:00am - 11:30am</p><p><svg width="11" height="12" viewBox="0 0 11 12" fill="#444"><path d="M5.5 0A4 4 0 0 0 1.5 4c0 3 4 8 4 8s4-5 4-8a4 4 0 0 0-4-4zm0 5.6A1.6 1.6 0 1 1 5.5 2.4a1.6 1.6 0 0 1 0 3.2z"/></svg>Elmford Market, Mill Place , Elmford , Elmford , EF17 2RN</p></div></article>
  <article class="event regular"><div class="badge"><div class="m">DEC</div><div class="d">13</div></div><div class="event-info"><h4>Brew &amp; Connect - Elmford Market</h4><p><svg width="11" height="11" viewBox="0 0 11 11" fill="none" stroke="#444" stroke-width="1.2"><circle cx="5.5" cy="5.5" r="4.6"/><path d="M5.5 3v2.7l1.8 1.2"/></svg>Tuesday ,10:00am - 11:30am</p><p><svg width="11" height="12" viewBox="0 0 11 12" fill="#444"><path d="M5.5 0A4 4 0 0 0 1.5 4c0 3 4 8 4 8s4-5 4-8a4 4 0 0 0-4-4zm0 5.6A1.6 1.6 0 1 1 5.5 2.4a1.6 1.6 0 0 1 0 3.2z"/></svg>Elmford Market, Mill Place , Elmford , Elmford , EF17 2RN</p></div></article>
</div>

<aside>
  <form class="card form login" style="top:635px;height:153px">
    <div class="field">Your e-mail</div>
    <div class="login-row"><div class="field">Password</div><div class="btn">Log in</div></div>
    <div class="remember"><span class="box"></span>Remember me ·<span class="forgot">Forgot password?</span></div>
  </form>

  <form class="card form signup" style="top:807px;height:293px">
    <h3>New to Gather Diary? <span>Sign up</span></h3>
    <div class="field">Full name</div>
    <div class="field">E-mail</div>
    <div class="field">Password</div>
    <div class="btn">Sign up for Gather Diary</div>
  </form>

  <h2 class="section-title" style="left:710px;top:1138px">
    <svg width="18" height="18" viewBox="0 0 18 18" fill="none" stroke="#222" stroke-width="1.6"><circle cx="9" cy="9" r="3.5"/><path d="M9 1v3M9 14v3M1 9h3M14 9h3M3.3 3.3l2.1 2.1M12.6 12.6l2.1 2.1M3.3 14.7l2.1-2.1M12.6 5.4l2.1-2.1"/></svg>
    Ads
  </h2>
  <div class="ads-slot" role="img" aria-label="Advertising space"></div>

  <h2 class="section-title" style="left:710px;top:1433px">
    <svg width="18" height="14" viewBox="0 0 18 14" fill="none" stroke="#f2890f" stroke-width="1.6"><path d="M1 5l3-4h10l3 4-8 8z"/><path d="M1 5h16M6 1l3 12 3-12"/></svg>
    Premium Profile
  </h2>
  <div class="premium">
    <p class="lead">Event Organisers - Upgrade to Premium Profile for only £4.99/month!</p>
    <p class="body">Inclusion in Featured Events section and highlighting of your events, display of event photos and videos, direct booking and social networking links and more!</p>
    <a class="btn-outline">Find out more..</a>
  </div>
</aside>

<h2 class="section-title" style="left:503px;top:1874px">
  <svg width="26" height="16" viewBox="0 0 26 16"><rect x="0" y="0" width="26" height="16" rx="2" fill="#f4604a"/><path d="M13 3.5l1.2 3h3.2l-2.6 2 1 3.2-2.8-2-2.8 2 1-3.2-2.6-2h3.2z" fill="#fff"/></svg>
  Gather Blog
</h2>

<section class="blog">
  <article class="post" style="left:172px">
    <div class="photo" role="img" aria-label="Photo of antique brass opera glasses beside a leather case"></div>
    <p class="cat">Custom Category</p>
    <h4>Lorem ipsum dolor sit amet</h4>
    <p class="date">OCT 23, 2015</p>
    <p class="excerpt">Lorem ipsum dolor sit amet, consectetur adipiscing elit. Phasellus nisi diam, convallis sed sapien eu, aliquam pharetra odio. Ut aliquam interdum porttitor.</p>
  </article>
  <article class="post" style="left:465px">
    <div class="photo" role="img" aria-label="Photo of antique brass opera glasses beside a leather case"></div>
    <p class="cat">Custom Category</p>
    <h4>Lorem ipsum dolor sit amet</h4>
    <p class="date">OCT 23, 2015</p>
    <p class="excerpt">Lorem ipsum dolor sit amet, consectetur adipiscing elit. Phasellus nisi diam, convallis sed sapien eu, aliquam pharetra odio. Ut aliquam interdum porttitor.</p>
  </article>
  <article class="post" style="left:756px">
    <div class="photo" role="img" aria-label="Photo of antique brass opera glasses beside a leather case"></div>
    <p class="cat">Custom Category</p>
    <h4>Lorem ipsum dolor sit amet</h4>
    <p class="date">OCT 23, 2015</p>
    <p class="excerpt">Lorem ipsum dolor sit amet, consectetur adipiscing elit. Phasellus nisi diam, convallis sed sapien eu, aliquam pharetra odio. Ut aliquam interdum porttitor.</p>
  </article>
</section>

<a class="btn read-blog">READ OUR BLOG</a>

<footer class="footer">
  <span class="copy">© 2015 GATHER DIARY</span>
  <nav><a>About</a><a>Help</a><a>Terms</a><a>Privacy</a><a>Cookies</a><a>Ads info</a></nav>
</footer>

</body>
</html>
```